Ember Ridge Clearing postcard ( for direct mailing) and business card design

Design postcards/Business cards
Dale Horvick
Ember Ridge Clearing
482 Copperfern Rd Lewisville,NC 27023
(336) 555-0184 Dale@Emberridgeclearing.example

The postcard will be used for direct mailing to land owners and contractors to advertise our service. Pictures of the process and equipment along with a short summary of what we do. Business card should be contact info and logo.
Updates

The post cards could say something like this: Forestry Mulching machines are capable of clearing land of unwanted trees and brush with limited disturbance to soils or desirable vegetation. Traditional land clearing methods often present an increased risk of erosion by pushing over trees, uprooting the stump and roots, and substantially disturbing soils.In contrast, mulching the vegetation leaves the soil structure intact. The mulched material can be left on the ground and will act as an erosion barrier while returning nutrients back into the soil through decomposition. Over time, grass will naturally grow through the mulch and can be maintained with mowing.

Target Market(s)

Land owners and contractors who need vegetation cleared

Industry/Entity Type

Forestry Mulching

Requirements
Must have
• picture, brief description of service offered, contact info on postcard. Business card should have contact info and logo.
Nice to have
• I like contour lines as a background but I'd like to see other ideas.

```html
<!DOCTYPE html>
<html lang="en">
<head>
<meta charset="utf-8">
<title>Ember Ridge Clearing – Postcard and Business Card</title>
<link href="https://fonts.googleapis.com/css2?family=Montserrat:wght@400;500;600;700&display=swap" rel="stylesheet">
<style>
  :root{
    --backdrop:#555555;
    --paper:#ffffff;
    --ink:#1d1d1d;
    --green-dark:#167a32;
    --green-mid:#2ea548;
    --green-light:#3cb54d;
    --brand-green:#1c7a38;
    --panel-grey:#ececea;
    --forest-a:#6b5a48;
    --forest-b:#9c8c78;
    --forest-c:#4a3f33;
    --sky-a:#9bb3c9;
  }
  *{box-sizing:border-box;margin:0;padding:0}
  html,body{width:1200px;height:1200px;overflow:hidden}
  body{background:var(--backdrop);font-family:"Montserrat",Arial,sans-serif;color:var(--ink);position:relative}

  .card{position:absolute;background:var(--paper);overflow:hidden;box-shadow:8px 10px 14px rgba(0,0,0,.35)}
  .photo{position:absolute}
  .photo--framed{border:3px solid #fff}

  .wordmark{position:absolute;display:flex;align-items:center;gap:7px}
  .wordmark__square{background:var(--brand-green);flex:none}
  .wordmark__name{font-weight:700;color:var(--ink);text-transform:uppercase;letter-spacing:.06em}

  .contact-band{position:absolute;left:0;right:0;bottom:0;color:#fff;
    background:linear-gradient(90deg,var(--green-dark) 0%,var(--green-light) 45%,var(--green-mid) 75%,var(--green-dark) 100%)}
  .contact-band__who{position:absolute;left:48px;top:12px;font-size:12.5px;line-height:15.6px;font-weight:400;white-space:nowrap}
  .contact-band__name{font-size:16px;line-height:18px;font-weight:500}
  .contact-band__pin{position:absolute;left:30px;top:34px}
  .contact-band__divider{position:absolute;left:284px;top:14px;width:2px;height:63px;background:#fff}
  .contact-band__line{position:absolute;left:318px;display:flex;align-items:center;gap:9px;font-size:13.5px;font-weight:400;white-space:nowrap}
  .contact-band__email{font-size:12.4px}

  /* front postcard */
  .postcard-front{left:68px;top:150px;width:587px;height:455px}
  .postcard-front .hero{left:0;top:0;width:230px;height:365px;
    background:linear-gradient(160deg,var(--forest-b) 0%,var(--forest-a) 45%,var(--forest-c) 100%)}
  .postcard-front .fade{left:230px;top:225px;width:357px;height:140px;
    background:linear-gradient(180deg,rgba(255,255,255,1) 0%,rgba(180,170,160,.6) 40%,var(--forest-a) 100%)}
  .postcard-front .summary{position:absolute;left:248px;top:105px;width:320px;font-size:14.6px;line-height:17.5px}
  .postcard-front .shot-1{left:194px;top:245px;width:167px;height:128px;
    background:linear-gradient(180deg,#3a3226 0%,#5a4a38 60%,#8a6c4a 100%)}
  .postcard-front .shot-2{left:380px;top:245px;width:167px;height:128px;
    background:linear-gradient(180deg,var(--sky-a) 0%,#a79a80 50%,#6e5e48 100%)}
  .postcard-front .contact-band{height:90px}

  /* back postcard */
  .postcard-back{left:75px;top:645px;width:580px;height:450px}
  .postcard-back .crew-shot{left:0;top:0;width:340px;height:204px;
    background:linear-gradient(180deg,#8a7a66 0%,#9a9288 45%,#b9b9b9 100%)}
  .postcard-back .machine-shot{left:1px;top:84px;width:140px;height:140px;
    background:linear-gradient(180deg,var(--sky-a) 0%,#a59a84 50%,#6a5a46 100%)}
  .postcard-back .story-panel{position:absolute;left:0;width:340px;background:var(--panel-grey)}
  .postcard-back .story{position:absolute;left:14px;top:228px;width:324px;font-size:12.6px;line-height:15.5px}
  .postcard-back .stamp{position:absolute;left:514px;top:15px;width:51px;height:47px;background:#ebebeb}
  .postcard-back .address-line{position:absolute;left:383px;width:183px;height:1.5px;background:var(--ink)}
  .postcard-back .contact-band{height:88px}

  /* business card */
  .business-card{left:696px;top:826px;width:463px;height:265px;box-shadow:none;
    background:linear-gradient(125deg,#fff 0%,#fff 70%,#eef2ea 82%,#fff 88%,#eef1ea 100%)}
  .business-card__divider{position:absolute;left:185px;top:46px;width:1.5px;height:178px;background:var(--ink)}
  .business-card__name{position:absolute;left:228px;top:40px;font-size:20px;font-weight:600;color:var(--brand-green)}
  .business-card__row{position:absolute;left:208px;display:flex;align-items:flex-start;gap:6px;font-size:14.6px;line-height:18px;white-space:nowrap}
  .business-card__row svg{flex:none;margin-top:2px}
  .business-card__email{font-size:12.2px}
</style>
</head>
<body>

<!-- Front of postcard -->
<section class="card postcard-front">
  <div class="photo hero" role="img" aria-label="Forestry mulcher on a tracked loader cutting through a wooded lot"></div>
  <div class="photo fade" role="img" aria-label="Faded view of mulching equipment behind the text"></div>

  <div class="wordmark" style="left:335px;top:40px">
    <span class="wordmark__square" style="width:22px;height:22px"></span>
    <span class="wordmark__name" style="font-size:13.5px;line-height:15.5px">Ember Ridge<br>Clearing</span>
  </div>

  <p class="summary">Forestry Mulching is especially economical for smaller plots of land or areas with less access. When land needs to be cleared for adding roads, servicing pipelines, or creating recreational spaces in a wooded area, forestry mulching can be a very effective method of clearing spaces.</p>

  <div class="photo photo--framed shot-1" role="img" aria-label="Front view of a mulching head on a tracked machine in the woods"></div>
  <div class="photo photo--framed shot-2" role="img" aria-label="Tracked loader with mulcher clearing brush in a field"></div>

  <div class="contact-band">
    <svg class="contact-band__pin" width="12" height="16" viewBox="0 0 12 16"><path d="M6 0a6 6 0 0 0-6 6c0 4.5 6 10 6 10s6-5.5 6-10a6 6 0 0 0-6-6z" fill="#fff"/><circle cx="6" cy="6" r="2.4" fill="var(--green-mid)"/></svg>
    <div class="contact-band__who">
      <div class="contact-band__name">Dale Horvick</div>
      Ember Ridge Clearing<br>482 Copperfern Rd Lewisville,<br>NC 27023
    </div>
    <div class="contact-band__divider"></div>
    <div class="contact-band__line" style="top:16px;left:314px">
      <svg width="16" height="16" viewBox="0 0 16 16"><circle cx="8" cy="8" r="7" fill="none" stroke="#fff" stroke-width="1.2"/><path d="M5.3 4.4l1.3-.2.7 1.8-.8.7a5 5 0 0 0 2.6 2.6l.7-.8 1.8.7-.2 1.3c-3.6.4-6.5-2.5-6.1-6.1z" fill="#fff"/></svg>
      (336) 555-0184
    </div>
    <div class="contact-band__line contact-band__email" style="top:43px;left:315px">
      <svg width="14" height="10" viewBox="0 0 14 10"><rect width="14" height="10" fill="#fff"/><path d="M0 0l7 5.5L14 0" fill="none" stroke="var(--green-mid)" stroke-width="1.3"/></svg>
      Dale@Emberridgeclearing.example
    </div>
  </div>
</section>

<!-- Back of postcard -->
<section class="card postcard-back">
  <div class="photo crew-shot" role="img" aria-label="Owner standing with two dogs beside a loaded equipment trailer"></div>
  <div class="photo photo--framed machine-shot" role="img" aria-label="Tracked loader with mulcher attachment in brush"></div>

  <div class="story-panel" style="top:224px;height:138px"></div>
  <div class="story-panel" style="top:204px;left:141px;width:199px;height:20px"></div>
  <p class="story">Along with making space for planned projects, forestry mulching is also a great way to clear unwanted vegetation to allow more desirable food sources for local wildlife to flourish. Creating access to waterways that have become overgrown and clearing space for animals to gain new breeding grounds are other ways forestry mulching can be helpful.</p>

  <div class="wordmark" style="left:348px;top:19px">
    <span class="wordmark__square" style="width:16px;height:16px"></span>
    <span class="wordmark__name" style="font-size:10.5px;line-height:12px">Ember Ridge<br>Clearing</span>
  </div>
  <div class="stamp"></div>
  <div class="address-line" style="top:205px"></div>
  <div class="address-line" style="top:235px"></div>
  <div class="address-line" style="top:268px"></div>

  <div class="contact-band">
    <svg class="contact-band__pin" width="12" height="16" viewBox="0 0 12 16" style="left:32px"><path d="M6 0a6 6 0 0 0-6 6c0 4.5 6 10 6 10s6-5.5 6-10a6 6 0 0 0-6-6z" fill="#fff"/><circle cx="6" cy="6" r="2.4" fill="var(--green-mid)"/></svg>
    <div class="contact-band__who" style="left:48px">
      <div class="contact-band__name">Dale Horvick</div>
      Ember Ridge Clearing<br>482 Copperfern Rd Lewisville,<br>NC 27023
    </div>
    <div class="contact-band__divider" style="left:278px"></div>
    <div class="contact-band__line" style="top:16px;left:309px">
      <svg width="16" height="16" viewBox="0 0 16 16"><circle cx="8" cy="8" r="7" fill="none" stroke="#fff" stroke-width="1.2"/><path d="M5.3 4.4l1.3-.2.7 1.8-.8.7a5 5 0 0 0 2.6 2.6l.7-.8 1.8.7-.2 1.3c-3.6.4-6.5-2.5-6.1-6.1z" fill="#fff"/></svg>
      (336) 555-0184
    </div>
    <div class="contact-band__line contact-band__email" style="top:43px;left:310px">
      <svg width="14" height="10" viewBox="0 0 14 10"><rect width="14" height="10" fill="#fff"/><path d="M0 0l7 5.5L14 0" fill="none" stroke="var(--green-mid)" stroke-width="1.3"/></svg>
      Dale@Emberridgeclearing.example
    </div>
  </div>
</section>

<!-- Business card -->
<section class="card business-card">
  <div class="wordmark" style="left:29px;top:108px">
    <span class="wordmark__square" style="width:20px;height:20px"></span>
    <span class="wordmark__name" style="font-size:12.5px;line-height:15px">Ember Ridge<br>Clearing</span>
  </div>
  <div class="business-card__divider"></div>
  <div class="business-card__name">Dale Horvick</div>
  <div class="business-card__row" style="top:70px">
    <svg width="14" height="16" viewBox="0 0 12 16"><path d="M6 0a6 6 0 0 0-6 6c0 4.5 6 10 6 10s6-5.5 6-10a6 6 0 0 0-6-6z" fill="var(--brand-green)"/><circle cx="6" cy="6" r="2.4" fill="#fff"/></svg>
    <span>Ember Ridge Clearing<br>482 Copperfern Rd<br>Lewisville,NC 27023</span>
  </div>
  <div class="business-card__row" style="top:150px">
    <svg width="15" height="15" viewBox="0 0 16 16"><circle cx="8" cy="8" r="7" fill="none" stroke="var(--brand-green)" stroke-width="1.3"/><path d="M5.3 4.4l1.3-.2.7 1.8-.8.7a5 5 0 0 0 2.6 2.6l.7-.8 1.8.7-.2 1.3c-3.6.4-6.5-2.5-6.1-6.1z" fill="var(--brand-green)"/></svg>
    <span>(336) 555-0184</span>
  </div>
  <div class="business-card__row business-card__email" style="top:191px">
    <svg width="13" height="10" viewBox="0 0 14 10" style="margin-top:3px"><rect width="14" height="10" fill="var(--brand-green)"/><path d="M0 0l7 5.5L14 0" fill="none" stroke="#fff" stroke-width="1.3"/></svg>
    <span>Dale@Emberridgeclearing.example</span>
  </div>
</section>

</body>
</html>
```